Business and Success Coaching Business Card

Need a business card for my coaching business. I coach small businesses, career professionals and, individuals wanting to unlock their human potential and achieve excellence. At the heart of our methodology is the Shaping Purposeful Action Routines Knowingly (SPARK) approach to formulate empowerment, create principles for success and setting achievable outcomes. I would like something that incorporates our new logo, something clean and sharp with a solid darker, but complementary background, color on the card front. The back should be white where there will be room for three questions

Target Market(s)

People looking to advance and improve themselves through a success coach

Industry/Entity Type

Life Coaching

Contact Information for Business Card

Contact information on card.
Business name on front of card
Questions on back

Font styles to use
Other font styles liked:
• Century Gothic or other Serif style fonts that look similar to Century Gothic

Colors

Designer to choose colors to be used in the design.

Requirements
Must have
• Logo on front of card
• Business name - The Steady Forge
• Contact name - Ted Harlow
• Address - Box 4619, Littleton, CO 80127-4619
• Phone number - 303-555-0147
• Email address - harlow.ted@thesteadyforge.example
• Certifications - CSC, CCHt, PTT, PNLP
• Back of card
• Three questions on the back of the card:
• If you were at your best, what would you do right now?
• What is the decision you have been avoiding?
• What's one action you could take in the next 10 minutes?
Nice to have
• I would like to see a solid color on the front of the card that compliments the logo.
• Back should be white, or could be contrasting, but need to have the three questions.

```html
<!DOCTYPE html>
<html lang="en">
<head>
<meta charset="utf-8">
<title>The Steady Forge – Business Card</title>
<link href="https://fonts.googleapis.com/css2?family=Open+Sans:wght@600;700&family=Questrial&display=swap" rel="stylesheet">
<style>
  :root {
    --navy: #1f3466;
    --navy-deep: #1a2c5a;
    --sky: #4786c6;
    --shadow-grey: #c9ccd2;
    --paper: #ffffff;
    --page: #eceef1;
    --edge: #b9bfcc;
  }
  * { box-sizing: border-box; margin: 0; padding: 0; }
  html, body { width: 1200px; height: 1199px; overflow: hidden; }
  body { background: var(--page); font-family: "Questrial", "Century Gothic", sans-serif; position: relative; }

  .card {
    position: absolute; left: 150px; width: 900px; height: 515px;
    background: var(--paper); border: 1px solid var(--edge); overflow: hidden;
  }
  .card--front { top: 55px; }
  .card--back { top: 629px; }
  .card__art { position: absolute; inset: 0; width: 100%; height: 100%; }

  .contact { position: absolute; color: var(--paper); }
  .contact__line { display: flex; align-items: center; gap: 10px; font-size: 20px; line-height: 30px; }
  .contact__line svg { width: 17px; height: 17px; fill: var(--paper); flex: none; }
  .contact--mail { left: 64px; top: 118px; }
  .contact--phone { left: 66px; top: 292px; }
  .contact--phone .contact__line { font-size: 37px; line-height: 50px; gap: 8px; }
  .contact--phone svg { width: 20px; height: 32px; }

  .brand { position: absolute; text-align: center; transform: translateX(-50%); }
  .brand__mark { display: block; margin: 0 auto 12px; width: 46px; height: 46px; border-radius: 50%; background: var(--sky); }
  .brand__name { font-family: "Open Sans", sans-serif; font-weight: 700; font-size: 28px; color: var(--navy); white-space: nowrap; }
  .card--front .brand { left: 693px; top: 242px; }
  .card--back .brand { left: 748px; top: 360px; }

  .holder { position: absolute; right: 66px; top: 370px; text-align: right; }
  .holder__name { font-family: "Open Sans", sans-serif; font-weight: 700; font-size: 56px; line-height: 64px; color: var(--navy); }
  .holder__creds { font-family: "Open Sans", sans-serif; font-weight: 600; font-size: 11px; color: var(--sky); margin-top: -6px; }

  .prompt-mark { position: absolute; left: 334px; top: 38px; transform: translateX(-50%); font-family: "Open Sans", sans-serif; font-weight: 700; font-size: 104px; line-height: 1; color: var(--paper); }
  .questions { position: absolute; left: 45px; top: 200px; list-style: none; color: var(--paper); font-style: italic; font-size: 19px; line-height: 28px; }
  .questions li::before { content: "•"; display: inline-block; width: 18px; font-style: normal; }
</style>
</head>
<body>

<section class="card card--front" aria-label="Card front">
  <svg class="card__art" viewBox="0 0 545 312" preserveAspectRatio="none" aria-hidden="true">
    <polygon points="419,0 429,0 236,312 222,312" fill="var(--shadow-grey)"/>
    <polygon points="399,0 419,0 222,312 203,312" fill="var(--navy-deep)"/>
    <polygon points="349,0 399,0 203,312 177,312" fill="var(--sky)"/>
    <polygon points="0,0 349,0 177,312 0,312" fill="var(--navy)"/>
  </svg>

  <div class="contact contact--mail">
    <p class="contact__line">
      <svg viewBox="0 0 16 16"><path d="M8 1 1 7h2v8h4v-5h2v5h4V7h2z"/></svg>
      Box 4619, Littleton, CO 80127-4619
    </p>
    <p class="contact__line">
      <svg viewBox="0 0 16 16"><path d="M1 3h14v10H1z M2 4l6 5 6-5" fill="none" stroke="#fff" stroke-width="1.5"/></svg>
      harlow.ted@thesteadyforge.example
    </p>
  </div>

  <div class="contact contact--phone">
    <p class="contact__line">
      <svg viewBox="0 0 10 16"><rect x="0" y="0" width="10" height="16" rx="1.5"/><circle cx="5" cy="13.5" r="1" fill="#1f3466"/></svg>
      303-555-0147
    </p>
  </div>

  <div class="brand">
    <span class="brand__mark" aria-hidden="true"></span>
    <p class="brand__name">The Steady Forge</p>
  </div>

  <div class="holder">
    <p class="holder__name">Ted Harlow</p>
    <p class="holder__creds">CSC, CCHt, PTT, PNLP</p>
  </div>
</section>

<section class="card card--back" aria-label="Card back">
  <svg class="card__art" viewBox="0 0 545 312" preserveAspectRatio="none" aria-hidden="true">
    <polygon points="545,0 545,6 298,312 290,312" fill="var(--shadow-grey)"/>
    <polygon points="0,0 545,0 290,312 0,312" fill="var(--navy)"/>
  </svg>

  <p class="prompt-mark">?</p>
  <ul class="questions">
    <li>If you were at your best, what would you do right now?</li>
    <li>What is the decision you have been avoiding?</li>
    <li>What’s one action you could take in the next 10 minutes?</li>
  </ul>

  <div class="brand">
    <span class="brand__mark" aria-hidden="true"></span>
    <p class="brand__name">The Steady Forge</p>
  </div>
</section>

</body>
</html>
```